Double-sided business card needed - specific brief

We need a double sided business card designed for our company Radiant Trimline. Having lost a lot of weight myself, the back of the card needs to show my before and after pictures. It needs to cover the entire back side of the card. This might be with my two before pictures over set on top of my main after picture or in separate frames. I'll leave that to your artistic consideration. The front needs to have our logo with contact details centred below.

The cards will be printed by PRINTKO.com and will be rectangular, 84mm x 55mm, but with ROUNDED edges. Please therefore present your designs rectangular but with rounded edges if possible.

The card should be designed in LANDSCAPE orientation.

As well as the logo, the front of the card should have the following details:

Moira Blakewell
Weight Loss Motivator with 189lb personal loss
moira@radiant-trimline.example
+44 (0)7700 900418

The website is important so should perhaps be more bold than the rest:
www.radiant-trimline.example

My brand colours are: Pink #CD2366, Light Pink #FD88AD. Blue #1C9CB1, Light Blue #64C4DE

Target Market(s)

Women 30+

Contact Information for Business Card

As description above

Font styles to use
Sans Serif

Requirements
Must have
• Double sided.
• Back side entirely covered with my before and after pictures.
• You may wish to float my before pictures on top of my after picture or add them in different frames. I look forward to seeing your different suggestions.

```html
<!DOCTYPE html>
<html lang="en">
<head>
<meta charset="utf-8">
<title>Radiant Trimline – Business Card</title>
<link href="https://fonts.googleapis.com/css2?family=Arimo:wght@400;700&family=Marcellus&display=swap" rel="stylesheet">
<style>
  :root{
    --pink:#b8195a;
    --pink-bright:#cd2366;
    --pink-light:#fd88ad;
    --blue:#1c9cb1;
    --blue-light:#64c4de;
    --blue-band:#5bb8d4;
    --card:#ffffff;
    --card-shade:#ececec;
    --ink:#222222;
    --stage:#2e2e2e;
  }
  *{margin:0;padding:0;box-sizing:border-box}
  html,body{width:1200px;height:997px;overflow:hidden}
  body{background:var(--stage);font-family:"Arimo",Arial,sans-serif;position:relative}

  .card{position:absolute;width:600px;height:393px;border-radius:24px;overflow:hidden;
    background:linear-gradient(135deg,var(--card) 0%,var(--card) 55%,var(--card-shade) 100%);
    box-shadow:0 18px 40px rgba(0,0,0,.55)}
  .card-back{left:70px;top:60px}
  .card-front{left:530px;top:510px}

  .card-art{position:absolute;inset:0}

  /* back side */
  .back-wordmark{position:absolute;left:34px;top:40px;font-family:"Marcellus",serif;color:var(--pink-bright);line-height:1}
  .back-wordmark .word-main{display:block;font-size:46px;letter-spacing:2px}
  .back-wordmark .word-sub{display:block;font-size:20px;letter-spacing:3px;margin-left:150px;margin-top:4px}
  .tab-label{position:absolute;color:#fff;font-size:16px}
  .tab-before{left:18px;bottom:12px}
  .tab-after{right:16px;top:184px}

  /* front side */
  .brand{position:absolute;left:0;right:0;top:70px;display:flex;align-items:center;justify-content:center;gap:14px}
  .brand-dot{width:34px;height:34px;border-radius:50%;background:var(--pink-bright)}
  .brand-name{font-family:"Marcellus",serif;font-size:44px;letter-spacing:2px;color:var(--pink-bright);text-transform:uppercase}

  .contact-block{position:absolute;left:318px;top:212px;width:282px;height:88px;background:var(--blue-band);
    padding:16px 0 0 32px;display:flex;flex-direction:column;gap:14px}
  .contact-row{display:flex;align-items:center;gap:12px;font-size:15px;color:var(--ink)}
  .contact-icon{width:14px;height:14px;flex:none}

  .person-block{position:absolute;left:0;top:262px;width:290px;height:92px;background:var(--pink);
    padding:14px 0 0 54px;color:#fff}
  .person-name{font-size:19px;font-weight:700;letter-spacing:.5px;text-transform:uppercase}
  .person-role{font-size:15px;line-height:1.25;margin-top:8px;margin-left:-10px}

  .website{position:absolute;left:298px;right:14px;top:326px;text-align:right;white-space:nowrap;
    font-size:14px;font-weight:700;letter-spacing:1px;color:var(--pink)}
</style>
</head>
<body>

<!-- Back side: before / after -->
<section class="card card-back" aria-label="Card back, before and after">
  <svg class="card-art" viewBox="0 0 600 393" width="600" height="393">
    <defs>
      <linearGradient id="before-tone" x1="0" y1="0" x2="1" y2="1">
        <stop offset="0" stop-color="#e9e2dc"/>
        <stop offset="1" stop-color="#b78a72"/>
      </linearGradient>
      <linearGradient id="after-tone" x1="0" y1="0" x2="1" y2="1">
        <stop offset="0" stop-color="#d8d5cf"/>
        <stop offset="1" stop-color="#8f8a80"/>
      </linearGradient>
    </defs>
    <rect x="440" y="170" width="160" height="42" fill="var(--blue)"/>
    <circle cx="415" cy="120" r="95" fill="var(--blue)"/>
    <circle cx="415" cy="120" r="80" fill="url(#after-tone)" role="img" aria-label="After photo of the founder"/>
    <rect x="0" y="350" width="190" height="43" fill="var(--pink-bright)"/>
    <path d="M140 350 Q165 372 200 350 Z" fill="var(--pink-bright)"/>
    <circle cx="165" cy="255" r="112" fill="var(--pink-bright)"/>
    <circle cx="165" cy="255" r="94" fill="url(#before-tone)" role="img" aria-label="Before photo of the founder"/>
  </svg>
  <div class="back-wordmark">
    <span class="word-main">RADIANT</span>
    <span class="word-sub">TRIMLINE</span>
  </div>
  <span class="tab-label tab-before">Before</span>
  <span class="tab-label tab-after">After</span>
</section>

<!-- Front side: brand and contact -->
<section class="card card-front" aria-label="Card front, contact details">
  <svg class="card-art" viewBox="0 0 600 393" width="600" height="393" aria-hidden="true">
    <line x1="318" y1="204" x2="600" y2="204" stroke="var(--blue-band)" stroke-width="2"/>
    <line x1="0" y1="359" x2="600" y2="359" stroke="var(--pink)" stroke-width="2"/>
    <line x1="0" y1="366" x2="600" y2="366" stroke="var(--pink)" stroke-width="2"/>
  </svg>

  <div class="brand">
    <span class="brand-dot"></span>
    <span class="brand-name">Radiant Trimline</span>
  </div>

  <div class="contact-block">
    <div class="contact-row">
      <svg class="contact-icon" viewBox="0 0 16 16"><circle cx="8" cy="8" r="8" fill="#333"/><path d="M5 4c1 0 1.5 2 1 2.5S6 8 8 10s2.5 1 3 1 1 1.5 0 1.5C8 12.5 3.5 8 4 5c0-.6.4-1 1-1z" fill="#fff"/></svg>
      <span>+44 (0)7700 900418</span>
    </div>
    <div class="contact-row">
      <svg class="contact-icon" viewBox="0 0 16 16"><circle cx="8" cy="8" r="8" fill="#333"/><path d="M4 6h8v5H4z" fill="#fff"/><path d="M4 6l4 3 4-3" stroke="#333" fill="none"/></svg>
      <span>moira@radiant-trimline.example</span>
    </div>
  </div>

  <div class="person-block">
    <div class="person-name">Moira Blakewell</div>
    <div class="person-role">Weight Loss Motivator<br>with 189lb personal loss</div>
  </div>

  <div class="website">www.radiant-trimline.example</div>
</section>

</body>
</html>
```